Business Card Design needed for logo design project

This project is linked to Maple Ridge Engineering need a logo and business card..

Our company needs a Business Card Design. Please refer to our original project in the link above.

```html
<!DOCTYPE html>
<html lang="en">
<head>
<meta charset="utf-8">
<title>Maple Ridge Engineering — Business Card</title>
<link href="https://fonts.googleapis.com/css2?family=Open+Sans:wght@400;600;700&display=swap" rel="stylesheet">
<style>
  :root {
    --leaf-green: #7bb52e;
    --brand-blue: #1f5de0;
    --ink: #4a4a4a;
    --soft-ink: #5c5c5c;
    --panel-grey: #a3a4a8;
    --card-white: #ffffff;
    --backdrop: #e4e4e2;
  }
  html, body {
    margin: 0;
    padding: 0;
    width: 1200px;
    height: 900px;
    overflow: hidden;
    background: var(--backdrop);
    font-family: "Open Sans", Arial, sans-serif;
  }
  .stage {
    position: relative;
    width: 1200px;
    height: 900px;
  }
  .card {
    position: absolute;
    left: 290px;
    width: 620px;
    height: 355px;
    background: var(--card-white);
    border-radius: 22px;
    overflow: hidden;
    box-shadow: 0 6px 18px rgba(0,0,0,0.12);
  }
  .card--front { top: 60px; }
  .card--back { top: 480px; }

  /* Front */
  .brand {
    position: absolute;
    left: 0; right: 0;
    top: 128px;
    display: flex;
    justify-content: center;
    align-items: center;
    gap: 14px;
  }
  .brand__dot {
    width: 26px;
    height: 26px;
    border-radius: 50%;
    background: var(--leaf-green);
  }
  .brand__name {
    font-weight: 700;
    font-size: 36px;
    color: var(--leaf-green);
    letter-spacing: 0.2px;
  }
  .front__web {
    position: absolute;
    left: 0; right: 0;
    top: 196px;
    text-align: center;
    font-size: 15px;
    letter-spacing: 6px;
    color: var(--soft-ink);
  }

  /* Back */
  .corner-panel {
    position: absolute;
    right: 0;
    bottom: 0;
    width: 620px;
    height: 355px;
  }
  .contact {
    position: absolute;
    left: 48px;
    top: 38px;
  }
  .contact__name {
    margin: 0;
    font-size: 22px;
    font-weight: 700;
    color: var(--leaf-green);
  }
  .contact__role {
    margin: 2px 0 16px;
    font-size: 16px;
    color: var(--brand-blue);
  }
  .contact__address {
    margin: 0 0 12px 30px;
    font-size: 15px;
    line-height: 21px;
    color: var(--ink);
  }
  .contact__list {
    list-style: none;
    margin: 0;
    padding: 0;
  }
  .contact__item {
    display: flex;
    align-items: center;
    gap: 12px;
    font-size: 15px;
    line-height: 24px;
    color: var(--ink);
  }
  .contact__icon {
    width: 18px;
    height: 18px;
    flex: none;
  }
  .contact__icon * { fill: var(--leaf-green); }
</style>
</head>
<body>
<main class="stage">

  <section class="card card--front" aria-label="Card front">
    <div class="brand">
      <span class="brand__dot"></span>
      <span class="brand__name">Maple Ridge Engineering</span>
    </div>
    <div class="front__web">www.mapleridge-eng.com</div>
  </section>

  <section class="card card--back" aria-label="Card back">
    <svg class="corner-panel" viewBox="0 0 620 355" aria-hidden="true">
      <path d="M400 355 C470 330 520 250 515 170 L520 120 L620 120 L620 355 Z" fill="var(--panel-grey)"/>
    </svg>

    <div class="contact">
      <h1 class="contact__name">Daniel Reyes</h1>
      <p class="contact__role">Director</p>
      <p class="contact__address">Suite 210 Cedar Avenue<br>Winnipeg, MB R3C 2E6, Canada</p>
      <ul class="contact__list">
        <li class="contact__item">
          <svg class="contact__icon" viewBox="0 0 20 20"><path d="M2 7c0-3 3-4 8-4s8 1 8 4v2h-4V7H6v2H2z"/><path d="M5 10h10l2 7H3z"/></svg>
          204 555 0187
        </li>
        <li class="contact__item">
          <svg class="contact__icon" viewBox="0 0 20 20"><path d="M6 1h8a1 1 0 0 1 1 1v16a1 1 0 0 1-1 1H6a1 1 0 0 1-1-1V2a1 1 0 0 1 1-1zm1 2v12h6V3z"/></svg>
          204 555 0142
        </li>
        <li class="contact__item">
          <svg class="contact__icon" viewBox="0 0 20 20"><path d="M5 2h10v5H5z"/><path d="M2 8h16v8h-3v-3H5v3H2z"/><path d="M6 14h8v4H6z"/></svg>
          204 555 0163
        </li>
        <li class="contact__item">
          <svg class="contact__icon" viewBox="0 0 20 20"><path d="M1 4h18v12H1zm2 2v1l7 5 7-5V6l-7 5z"/></svg>
          info@mapleridge-eng.com
        </li>
        <li class="contact__item">
          <svg class="contact__icon" viewBox="0 0 20 20"><path d="M10 1a9 9 0 1 0 0 18 9 9 0 0 0 0-18zM3 9h3.5c.1-2 .5-3.7 1.2-5A7 7 0 0 0 3 9zm5.5 0h3c-.1-2.5-.8-4.5-1.5-5.2C9.3 4.5 8.6 6.5 8.5 9zm5 0H17a7 7 0 0 0-4.7-5c.7 1.3 1.1 3 1.2 5zM3 11a7 7 0 0 0 4.7 5c-.7-1.3-1.1-3-1.2-5zm5.5 0c.1 2.5.8 4.5 1.5 5.2.7-.7 1.4-2.7 1.5-5.2zm5 0c-.1 2-.5 3.7-1.2 5A7 7 0 0 0 17 11z"/></svg>
          www.mapleridge-eng.com
        </li>
      </ul>
    </div>
  </section>

</main>
</body>
</html>
```